Business Card Design

We need a design that will also transfer to car decals
We need a design that will speak to the average person needing home and office remodeling
The design should be fresh, exciting, easy to read in a glance and unique
We would like a die-cut tool belt
Bright colors and evenly spaced information

Target Market(s)

Home and business owners
Middle and Upper Income property owners
Families and people with fixer upper homes

Industry/Entity Type

Business

Contact Information for Business Card

Looking for the best Bay Area Handyman? Here I am!
RKW Handyman Services does it all at prices regular people can afford.
Electrical, Plumbing, Carpentry, Remodeling, Fencing, Picture and window placement, Hauling ... and anything else you can imagine!
510-374-2196
Serving the Entire Bay Area
Free Estimates! Call us Today to turn your dreams into reality!

Font styles to use
Serif

Requirements
Must have
• Speaks to the average person
stands out among similar industry cards
Nice to have
• fun, comical, you want to hold on to this card
Should not have
• bland colors
look too crowded

```html
<!DOCTYPE html>
<html lang="en">
<head>
<meta charset="utf-8">
<title>RKW Handyman Services – Business Card</title>
<link rel="stylesheet" href="https://fonts.googleapis.com/css2?family=Roboto+Slab:wght@800&family=Signika:wght@600&display=swap">
<style>
  :root {
    --ink-frame: #595959;
    --paper: #ffffff;
    --brand-blue: #3ba4dc;
    --accent-red: #e4373f;
    --steel-light: #e2e2e2;
    --steel-mid: #a8a8a8;
    --steel-dark: #8f8f8f;
    --belt-grey: #666666;
    --handle-blue: #3aa9e0;
    --ruler-yellow: #f2e300;
    --handle-tan: #b89462;
  }
  * { margin: 0; padding: 0; box-sizing: border-box; }
  html, body {
    width: 1011px;
    height: 1200px;
    overflow: hidden;
    background: var(--paper);
    font-family: "Signika", "Trebuchet MS", sans-serif;
  }
  .canvas { position: relative; width: 1011px; height: 1200px; }

  .card {
    position: absolute;
    background: var(--paper);
    border-style: solid;
    border-color: var(--ink-frame);
  }
  .card--front { left: 62px; top: 30px; width: 885px; height: 526px; border-width: 8px; }
  .card--front::after {
    content: ""; position: absolute; inset: 0; border: 1.5px solid #222;
  }
  .card--back { left: 58px; top: 613px; width: 894px; height: 531px; border-width: 13px; }

  .artwork { position: absolute; display: block; }

  .front__nut  { left: 80px;  top: 37px;  width: 222px; height: 183px; }
  .front__belt { left: 383px; top: 60px;  width: 411px; height: 233px; }

  .brand__mark {
    position: absolute; left: 0; width: 420px; top: 248px;
    text-align: center;
    font-family: "Roboto Slab", Georgia, serif;
    font-weight: 800; font-size: 80px; letter-spacing: 10px;
    color: var(--brand-blue); line-height: 1;
  }
  .brand__tagline {
    position: absolute; left: 0; width: 420px; top: 360px;
    text-align: center; font-weight: 600; font-size: 42px; line-height: 54px;
    color: var(--brand-blue);
  }
  .front__cta {
    position: absolute; left: 419px; top: 364px;
    font-weight: 600; font-size: 44px; color: var(--accent-red); line-height: 1;
  }
  .front__phone {
    position: absolute; left: 424px; top: 411px;
    font-weight: 600; font-size: 64px; color: var(--accent-red); line-height: 1;
  }

  .back__wrench { left: 85px;  top: 49px; width: 391px; height: 116px; }
  .back__nut    { left: 623px; top: 29px; width: 175px; height: 145px; }

  .back__headline {
    position: absolute; left: 0; right: 0; top: 215px;
    text-align: center; font-weight: 600; font-size: 26px; line-height: 34px;
    color: var(--accent-red);
  }
  .back__services {
    position: absolute; left: 20px; right: 20px; top: 261px;
    text-align: center; font-weight: 600; font-size: 26px; line-height: 38px;
    color: var(--brand-blue);
  }
  .back__cta {
    position: absolute; left: 140px; top: 436px;
    font-weight: 600; font-size: 26px; color: var(--accent-red);
  }
  .back__phone {
    position: absolute; left: 338px; top: 402px;
    font-weight: 600; font-size: 64px; color: var(--accent-red); line-height: 1;
  }
</style>
</head>
<body>
<main class="canvas">

  <section class="card card--front">
    <svg class="artwork front__nut" viewBox="0 0 222 183" role="img" aria-label="Illustration of a grey hex nut">
      <defs>
        <linearGradient id="nutTonesFront" x1="0" y1="0" x2="1" y2="1">
          <stop offset="0" stop-color="var(--steel-mid)"/>
          <stop offset="0.35" stop-color="var(--steel-light)"/>
          <stop offset="1" stop-color="#d2d2d2"/>
        </linearGradient>
      </defs>
      <rect width="222" height="183" rx="30" fill="url(#nutTonesFront)"/>
    </svg>
    <svg class="artwork front__belt" viewBox="0 0 411 233" role="img" aria-label="Illustration of a tool belt holding a blue screwdriver, a wrench, a yellow ruler and a hammer">
      <defs>
        <linearGradient id="beltTones" x1="0" y1="0" x2="1" y2="0">
          <stop offset="0" stop-color="var(--belt-grey)"/>
          <stop offset="0.2" stop-color="var(--handle-blue)"/>
          <stop offset="0.4" stop-color="var(--steel-mid)"/>
          <stop offset="0.6" stop-color="var(--ruler-yellow)"/>
          <stop offset="0.8" stop-color="var(--handle-tan)"/>
          <stop offset="1" stop-color="var(--belt-grey)"/>
        </linearGradient>
      </defs>
      <rect width="411" height="233" rx="22" fill="url(#beltTones)"/>
    </svg>

    <div class="brand__mark">RKW</div>
    <div class="brand__tagline">handyman<br>services</div>

    <div class="front__cta">call us today :</div>
    <div class="front__phone">510-374-2196</div>
  </section>

  <section class="card card--back">
    <svg class="artwork back__wrench" viewBox="0 0 391 116" role="img" aria-label="Illustration of a grey open-end wrench">
      <defs>
        <linearGradient id="wrenchTones" x1="0" y1="0" x2="1" y2="0">
          <stop offset="0" stop-color="var(--steel-mid)"/>
          <stop offset="0.5" stop-color="var(--steel-light)"/>
          <stop offset="1" stop-color="var(--steel-mid)"/>
        </linearGradient>
      </defs>
      <rect width="391" height="116" rx="40" fill="url(#wrenchTones)"/>
    </svg>
    <svg class="artwork back__nut" viewBox="0 0 175 145" role="img" aria-label="Illustration of a grey hex nut">
      <defs>
        <linearGradient id="nutTonesBack" x1="0" y1="0" x2="1" y2="1">
          <stop offset="0" stop-color="var(--steel-mid)"/>
          <stop offset="0.35" stop-color="var(--steel-light)"/>
          <stop offset="1" stop-color="#d2d2d2"/>
        </linearGradient>
      </defs>
      <rect width="175" height="145" rx="24" fill="url(#nutTonesBack)"/>
    </svg>

    <p class="back__headline">Looking for the best Bay Area Handyman? Here I am!</p>
    <p class="back__services">we do it all at prices regular people can afford. Electrical, Plumbing,<br>Carpentry, Remodeling, Fencing, Picture andwindow placement,<br>Hauling ... and anything else you can imagine!</p>

    <div class="back__cta">callus today :</div>
    <div class="back__phone">510-374-2196</div>
  </section>

</main>
</body>
</html>
```